Canadian Christian Church needs design for new sermon series

A graphic design for our series and an invitation card to invite people to the series. Check design brief for more detailed information. Target audience: young families and young adults. Looking for a creative design that will get people's attention and create interest. See design brief for copy of design purchased for previous series.
entered Apr 4 incorrectly. Need a week to receive and review designs, and today is Apr 2/19. Thanks!
young families and young adults

```html
<!DOCTYPE html>
<html lang="en">
<head>
<meta charset="utf-8">
<title>Messy – Sermon Series Invitation Card</title>
<link href="https://fonts.googleapis.com/css2?family=Anton&family=Roboto+Slab:wght@400;500;700&family=Montserrat:wght@400;500;600&family=Cabin+Condensed:wght@400;500&display=swap" rel="stylesheet">
<style>
  :root {
    --backdrop: #e4e4e4;
    --ink: #2f2b29;
    --band: #3d3432;
    --beige-light: #d8d1bb;
    --beige: #c6bda1;
    --orange: #f7931e;
    --orange-deep: #e8711a;
    --purple: #6b2d7e;
    --blue: #1f6fc0;
    --white: #ffffff;
    --rule: #5a524a;
  }
  * { box-sizing: border-box; margin: 0; padding: 0; }
  html, body { width: 1200px; height: 903px; overflow: hidden; }
  body { background: var(--backdrop); position: relative; font-family: "Montserrat", sans-serif; }

  .card {
    position: absolute; width: 482px; height: 378px; overflow: hidden;
    box-shadow: 0 2px 6px rgba(0,0,0,0.18);
  }

  /* Front */
  .card-front { left: 177px; top: 60px; }
  .front-photo {
    position: absolute; inset: 0;
    background:
      radial-gradient(ellipse at 15% 10%, #dfe8c8 0%, rgba(223,232,200,0) 30%),
      radial-gradient(ellipse at 70% 70%, rgba(60,90,150,0.55) 0%, rgba(60,90,150,0) 35%),
      linear-gradient(160deg, #8a9a78 0%, #4f6a52 35%, #3b4a3a 60%, #2a2a24 100%);
  }
  .church-name {
    position: absolute; left: 24px; top: 36px; display: flex; align-items: center; gap: 6px;
    font-family: "Cabin Condensed", sans-serif; font-size: 13px; color: var(--ink); white-space: nowrap;
  }
  .church-name .dot { width: 14px; height: 14px; border-radius: 50%; background: var(--orange); }
  .series-title {
    position: absolute; left: 258px; top: 24px; width: 210px; text-align: center;
    font-family: "Anton", sans-serif; font-size: 74px; font-weight: 400; line-height: 1; letter-spacing: 1px;
    background: linear-gradient(180deg, #ffd26a 0%, var(--orange) 55%, var(--orange-deep) 100%);
    -webkit-background-clip: text; background-clip: text; color: transparent;
    -webkit-text-stroke: 1.5px var(--purple);
  }
  .series-tagline {
    position: absolute; left: 0; width: 100%; top: 290px; text-align: center; white-space: nowrap;
    font-family: "Roboto Slab", serif; font-size: 35px; font-weight: 400; line-height: 1; color: var(--orange);
    text-shadow: 1px 1px 2px rgba(0,0,0,0.8);
  }
  .front-band {
    position: absolute; left: 0; bottom: 0; width: 100%; height: 41px; background: var(--band);
    color: var(--white); font-family: "Roboto Slab", serif; font-size: 22px; white-space: nowrap;
    display: flex; align-items: center; justify-content: center;
  }

  /* Back */
  .card-back {
    left: 582px; top: 469px;
    background: radial-gradient(ellipse at 60% 45%, var(--beige-light) 0%, var(--beige) 75%);
  }
  .service-title {
    position: absolute; top: 22px; width: 100%; text-align: center; white-space: nowrap;
    font-family: "Roboto Slab", serif; font-weight: 700; color: var(--ink);
    font-size: 26px; line-height: 32px;
  }
  .service-title .time { display: block; font-size: 26px; }
  .section-heading {
    position: absolute; left: 26px; font-size: 12px; font-weight: 600; color: var(--ink);
    line-height: 14px; white-space: nowrap;
  }
  .sermon-table {
    position: absolute; left: 27px; top: 119px; width: 227px;
    border-collapse: collapse; font-size: 11px; color: var(--ink); white-space: nowrap;
  }
  .sermon-table td { border: 1px solid var(--rule); height: 16px; padding: 0 0 0 8px; line-height: 14px; }
  .sermon-table td.date { width: 73px; }
  .features {
    position: absolute; left: 28px; top: 276px; list-style: none; font-size: 11px; color: var(--ink); white-space: nowrap;
  }
  .features li { display: flex; align-items: center; gap: 6px; height: 15px; }
  .values-graphic {
    position: absolute; left: 290px; top: 110px; width: 170px; height: 164px;
    background: conic-gradient(from 20deg, var(--orange) 0 20%, var(--blue) 20% 40%, var(--orange) 40% 60%, var(--purple) 60% 80%, var(--blue) 80% 100%);
    border-radius: 50%;
    -webkit-mask: radial-gradient(circle, transparent 32%, #000 33%);
            mask: radial-gradient(circle, transparent 32%, #000 33%);
  }
  .back-band {
    position: absolute; left: 0; bottom: 0; width: 100%; height: 56px; background: var(--band);
    color: var(--white); font-family: "Cabin Condensed", sans-serif; font-size: 11px;
  }
  .contact-line { position: absolute; display: flex; align-items: center; gap: 5px; white-space: nowrap; line-height: 14px; }
  .contact-line svg { width: 9px; height: 9px; flex: none; }
  .contact-line .web { display: flex; align-items: center; gap: 5px; margin-left: 10px; }
  .contact-person { position: absolute; left: 288px; top: 11px; line-height: 14px; white-space: nowrap; }
  .contact-person .email { display: block; margin-top: 2px; color: var(--orange); }
</style>
</head>
<body>

<section class="card card-front">
  <div class="front-photo" role="img" aria-label="Photograph of a cluttered room full of boxes, toys and stacked books"></div>
  <div class="church-name"><span class="dot"></span>Maple Grove Family Church</div>
  <h1 class="series-title">MESSY</h1>
  <p class="series-tagline">Joining God in the Mess</p>
  <div class="front-band">Connecting Young Families to Christ</div>
</section>

<section class="card card-back">
  <h2 class="service-title">THE TIME OF THE SERVICES:<span class="time">Sundays @ 10:30</span></h2>

  <p class="section-heading" style="top:100px">Names &amp; Dates of the sermons:</p>
  <table class="sermon-table">
    <tr><td class="date">April 28th:</td><td>We Made This Mess</td></tr>
    <tr><td class="date">May 5th:</td><td>Bless in the Mess</td></tr>
    <tr><td class="date">May 12th:</td><td>Born into the Mess</td></tr>
    <tr><td class="date">May 19th:</td><td>Messy Work</td></tr>
    <tr><td class="date">May 26th:</td><td>Messy Church</td></tr>
    <tr><td class="date">June 2nd:</td><td>Messy Hospitality</td></tr>
    <tr><td class="date">June 9th:</td><td>TBD</td></tr>
    <tr><td class="date">June 16th:</td><td>Messy within Boundaries</td></tr>
  </table>

  <div class="values-graphic" role="img" aria-label="Ribbon diagram of the church's core values: equipping, serving, missional living, spirit-living and belonging"></div>

  <p class="section-heading" style="top:260px">Features of the service:</p>
  <ul class="features">
    <li><svg width="9" height="9" viewBox="0 0 10 10"><circle cx="5" cy="5" r="5" fill="var(--blue)"/><path d="M2.8 5.2l1.5 1.5 3-3" stroke="#fff" stroke-width="1.4" fill="none"/></svg>Staffed nursery &amp; children’s program every Sunday</li>
    <li><svg width="9" height="9" viewBox="0 0 10 10"><circle cx="5" cy="5" r="5" fill="var(--blue)"/><path d="M2.8 5.2l1.5 1.5 3-3" stroke="#fff" stroke-width="1.4" fill="none"/></svg>Coffee &amp; snacks</li>
    <li><svg width="9" height="9" viewBox="0 0 10 10"><circle cx="5" cy="5" r="5" fill="var(--blue)"/><path d="M2.8 5.2l1.5 1.5 3-3" stroke="#fff" stroke-width="1.4" fill="none"/></svg>Everyone welcome</li>
  </ul>

  <footer class="back-band">
    <div class="contact-line" style="left:29px; top:11px">
      <svg viewBox="0 0 10 10"><path d="M5 0.5a3.3 3.3 0 0 0-3.3 3.3C1.7 6.3 5 9.5 5 9.5s3.3-3.2 3.3-5.7A3.3 3.3 0 0 0 5 0.5z" fill="none" stroke="var(--orange)" stroke-width="1.2"/><circle cx="5" cy="3.8" r="1.2" fill="var(--orange)"/></svg>
      1180 Cedar Ridge Road Oakville, ON L6H 2K4
    </div>
    <div class="contact-line" style="left:29px; top:31px">
      <svg viewBox="0 0 10 10"><path d="M2 0.8l1.8 2-1 1.2c.6 1.3 1.6 2.3 2.9 2.9l1.2-1 2 1.8-1.1 1.5C4.5 9 1 5.5.7 1.9z" fill="var(--orange)"/></svg>
      905-555-0148
      <span class="web">
        <svg viewBox="0 0 10 10"><circle cx="5" cy="5" r="4.3" fill="none" stroke="var(--orange)" stroke-width="1"/><path d="M0.7 5h8.6M5 0.7c-2.2 2.4-2.2 6.2 0 8.6M5 0.7c2.2 2.4 2.2 6.2 0 8.6" fill="none" stroke="var(--orange)" stroke-width="0.8"/></svg>
        www.maplegrovefamily.ca
      </span>
    </div>
    <div class="contact-person">
      Please contact Laura Pembrook
      <span class="email">worship@maplegrovefamily.ca</span>
    </div>
  </footer>
</section>

</body>
</html>
```